RM BIZ CARDS

Hi,

Is it possible to see a one sided version (with logo and info) as well as a two-sided version (front side w/logo and back side with info)?
How do we choose card stock and finish once we approve a design?

We would like the following info included:

Peter Lowell
Rosfeld Talent Media
4127 Marwick Lane, Suite 300
Los Angeles, CA 90041
(323) 555-0148
peter@rosfeldtalentmedia.example

```html
<!DOCTYPE html>
<html lang="en">
<head>
<meta charset="utf-8">
<title>Rosfeld Talent Media — Business Cards</title>
<link href="https://fonts.googleapis.com/css2?family=Montserrat:wght@300;400;600&display=swap" rel="stylesheet">
<style>
  :root {
    --backdrop: #3a3a3a;
    --card: #111111;
    --ink: #f2f2f2;
    --ink-soft: #cfcfcf;
    --rule: #8a8a8a;
  }
  * { margin: 0; padding: 0; box-sizing: border-box; }
  html, body {
    width: 1200px;
    height: 901px;
    overflow: hidden;
    background: var(--backdrop);
    font-family: "Montserrat", Arial, sans-serif;
    color: var(--ink);
  }
  .sheet {
    position: relative;
    width: 1200px;
    height: 901px;
    display: flex;
    align-items: center;
    justify-content: center;
    gap: 40px;
  }
  .card {
    position: relative;
    width: 540px;
    height: 309px;
    background: var(--card);
    box-shadow: 0 14px 30px rgba(0,0,0,0.45);
  }

  /* Front: brand side */
  .card-front {
    display: flex;
    align-items: center;
    justify-content: center;
    gap: 16px;
  }
  .brand-dot {
    width: 34px;
    height: 34px;
    border: 2px solid var(--ink);
    border-radius: 50%;
  }
  .brand-name {
    font-weight: 400;
    font-size: 26px;
    letter-spacing: 5px;
    text-transform: uppercase;
  }

  /* Back: contact side */
  .contact-name {
    position: absolute;
    left: 56px;
    top: 54px;
    font-weight: 300;
    font-size: 24px;
    letter-spacing: 1px;
    text-transform: uppercase;
  }
  .rule-horizontal {
    position: absolute;
    left: 56px;
    top: 104px;
    width: 380px;
    height: 1px;
    background: var(--rule);
  }
  .rule-vertical {
    position: absolute;
    left: 150px;
    top: 92px;
    width: 1px;
    height: 72px;
    background: var(--rule);
  }
  .contact-company {
    position: absolute;
    left: 160px;
    top: 112px;
    font-weight: 300;
    font-size: 12px;
    color: var(--ink-soft);
  }
  .contact-details {
    position: absolute;
    left: 56px;
    top: 178px;
    font-weight: 300;
    font-size: 13px;
    line-height: 1.5;
    color: var(--ink-soft);
    font-style: normal;
  }
  .contact-details strong {
    font-weight: 600;
    color: var(--ink);
    letter-spacing: 1px;
    text-transform: uppercase;
  }
  .back-mark {
    position: absolute;
    left: 446px;
    top: 92px;
    display: flex;
    align-items: center;
    gap: 6px;
  }
  .back-mark .brand-dot { width: 22px; height: 22px; border-width: 1.5px; }
  .back-mark span {
    font-weight: 400;
    font-size: 14px;
    letter-spacing: 2px;
  }
</style>
</head>
<body>
  <main class="sheet">
    <section class="card card-back" aria-label="Card back with contact details">
      <h1 class="contact-name">Peter Lowell</h1>
      <div class="rule-horizontal"></div>
      <div class="rule-vertical"></div>
      <p class="contact-company">Rosfeld Talent Media</p>
      <address class="contact-details">
        (323) 555-0148<br>
        peter@rosfeldtalentmedia.example<br>
        <strong>Rosfeld Talent</strong><br>
        4127 Marwick Lane, Suite 300<br>
        Los Angeles, CA 90041
      </address>
      <div class="back-mark">
        <div class="brand-dot"></div>
        <span>RM</span>
      </div>
    </section>

    <section class="card card-front" aria-label="Card front with brand name">
      <div class="brand-dot"></div>
      <p class="brand-name">Rosfeld Talent</p>
    </section>
  </main>
</body>
</html>
```